****FLYER design - LAW FIRM ADVERTISEMENT****

We are a small law firm based in Los Angeles, CA. We need an flyer used for advertising that we will be passing out. We want the flyer to be about 4in x 6in.

We want the flyer to advertise the name of our firm: MARVELLO QUINTARD LLP (no period)
- We want our group photo to take up a good portion of the flyer (although it's okay if parts of the photo have wording over it.)

COLORS: Our firm colors are different shades of steal/metal grey with a bit of a bold orange accent. Any bold writing, like our slogan, names of practice areas,... should be in orange.

We envision a horizontal lay-out of the flyer, but are open to creative options laid out vertically!

Feel free to play with the fonts, the sizing, the color combinations,...

We want the flyer to advertise our two areas of practice: PERSONAL INJURY and EMPLOYMENT LAW. Please also place each photo icon of our areas of practice somewhere around the name (ambulance photo for personal injury; person behind computer desk for employment law). The icons can be relatively small.

Under Personal Injury, please write:
If you or a loved one are suffering from an injury or wrongful death caused by the careless or intentional acts of others, then you have the right to pursue compensation for your injury, out-of-pocket expenses, lost wages, emotional anguish, and more.

Under Employment Law, please write:
Our attorneys regularly represent clients in disputes involving sex, age and race discrimination, sexual harassment, retaliatory discharge, defamation, unlawful termination, breach of employment contracts, and more.

Somewhere on the flyer, please write our slogan IN ITALICS (and probably in orange):
- You Speak. We Listen. They Pay.

In somewhat bright and bold writing, please write "CONTACT US FOR A FREE CONSULTATION TODAY!" (maybe just after our slogan?)
- And under that phrase, write:
- 752 W. Folbrook Lane, Suite 400 Beverly Hills, CA 90210
phone: 310.555.8143
fax: 310.555.9261
email: info@mqmlegal.example
web: www.mqmlegal.example

If possible, and only if there's room without it looking too busy, somewhere in the upper left corner, place our "MQM" logo.
Updates

PLEASE NOTE THAT WE CHANGED OUR GROUP PHOTO TO A SLIGHTLY EDITED ONE.  PLEASE BE SURE TO USE THE NEW ONE!!!  (We deleted the old.)

Target Market(s)

employees, lower and mid-income individuals, minority communities. However, we still want the flyer to look sleek, modern, and professional.

Industry/Entity Type

Advertising

Requirements
Must have
• Firm Name,
Photo of Partners,
Names, photos, and small description of practice areas,
Firm slogan,
"Contact us for a free consultation today!",
Firm contact info.

And only if space and overall look permits, firm "MQM" logo.

We want an overall very sleek, modern feel to our flyer. While we do want to look professional, we wanted a more approachable feel than the typical, conservative law offices.
Nice to have
• Firm "MQM" logo

Horizontal lay out, though we're open to vertical options.

```html
<!DOCTYPE html>
<html lang="en">
<head>
<meta charset="utf-8">
<title>Marvello Quintard LLP — Flyer</title>
<link rel="stylesheet" href="https://fonts.googleapis.com/css2?family=Cinzel:wght@600&family=PT+Sans:ital,wght@0,400;0,700;1,400;1,700&display=swap">
<style>
  :root {
    --page: #e9eaec;
    --ink-black: #0b0b0c;
    --steel-dark: #2b2f35;
    --steel: #4f555d;
    --steel-light: #9aa0a7;
    --silver: #e6e8ea;
    --orange: #f39a1e;
    --orange-deep: #d9730a;
    --orange-bright: #ffb23a;
    --gold: #f6b43a;
    --white: #ffffff;
  }
  * { box-sizing: border-box; margin: 0; padding: 0; }
  html, body { width: 1149px; height: 1200px; overflow: hidden; }
  body { background: var(--page); position: relative; font-family: "PT Sans", sans-serif; }

  .flyer {
    position: absolute; left: 40px; top: 237px;
    width: 1069px; height: 725px;
    background: var(--ink-black);
    overflow: hidden;
    box-shadow: 0 6px 18px rgba(0,0,0,.35);
  }
  .chrome-top {
    position: absolute; left: 0; top: 0; width: 100%; height: 55px;
    background: linear-gradient(180deg, #000 0 14px, #6c7278 14px 18px, #0f1012 18px 40px, #c9cdd1 40px 43px, #17181a 43px 100%);
  }
  .header-bar {
    position: absolute; left: 0; top: 55px; width: 100%; height: 62px;
    background: linear-gradient(180deg, #1a1b1d, #050505);
  }
  .firm-name {
    position: absolute; left: 58px; top: 62px;
    font-family: "Cinzel", serif; font-weight: 600; font-size: 34px;
    letter-spacing: 1px; color: var(--gold); line-height: 46px;
  }
  .accent-bar {
    position: absolute; left: 610px; top: 68px; width: 459px; height: 32px;
    background: linear-gradient(180deg, var(--orange-bright), var(--orange-deep));
  }
  .slogan-band {
    position: absolute; left: 0; top: 117px; width: 100%; height: 70px;
    background: linear-gradient(90deg, var(--silver) 0%, #cfd3d7 45%, #5a6068 75%, #2e3237 100%);
  }
  .slogan {
    position: absolute; left: 56px; top: 130px;
    font-style: italic; font-size: 34px; color: #222428; letter-spacing: -.5px;
  }
  .name-box {
    position: absolute; left: 855px; top: 39px; width: 155px; height: 164px;
    background: var(--steel);
    display: flex; align-items: center; justify-content: center;
    padding: 0 12px; text-align: center;
  }
  .name-box-text {
    font-family: "PT Sans", sans-serif; font-weight: 700; font-size: 19px;
    line-height: 24px; color: var(--white);
  }
  .main-panel {
    position: absolute; left: 0; top: 187px; width: 100%; height: 479px;
    background: radial-gradient(ellipse at 30% 40%, var(--orange-bright) 0%, var(--orange) 35%, var(--orange-deep) 75%, #8a4708 100%);
  }
  .contact-bar {
    position: absolute; left: 0; top: 517px; width: 100%; height: 40px;
    background: linear-gradient(90deg, rgba(0,0,0,0) 0%, #1a1b1d 45%, #0c0c0d 100%);
  }
  .contact-info {
    position: absolute; left: 600px; top: 557px; width: 469px; height: 109px;
    background: linear-gradient(180deg, #5b6169, #3a3f45);
    padding: 8px 20px 0 0;
    text-align: right; color: var(--silver); font-size: 14px; line-height: 19px;
  }
  .contact-info .address { font-style: italic; font-size: 12.5px; }
  .contact-info strong { color: var(--white); font-weight: 700; }
  .partner-photo {
    position: absolute; left: 0; top: 187px; width: 600px; height: 479px;
    background: radial-gradient(ellipse at 50% 55%, #f2efe9 0%, #b9a48c 35%, rgba(40,36,34,.85) 70%, rgba(217,115,10,0) 100%);
  }
  .practice-head {
    position: absolute; left: 655px; width: 414px; height: 29px;
    background: linear-gradient(180deg, #2a2d31, #111214);
    padding-left: 12px;
    font-family: "Cinzel", serif; font-weight: 600; font-size: 20px;
    color: var(--orange); line-height: 29px;
  }
  .practice-copy {
    position: absolute; left: 665px; width: 390px;
    font-style: italic; font-size: 16px; line-height: 18.5px; color: var(--white);
  }
  .practice-icon {
    position: absolute; left: 592px; width: 48px; height: 48px;
    background: #1d1f22; border: 2px solid #d8dadc;
  }
  .contact-callout {
    position: absolute; left: 540px; top: 522px;
    font-style: italic; font-weight: 700; font-size: 22px; color: var(--orange-bright);
    letter-spacing: .3px;
  }
  .contact-callout b { color: var(--orange); }
  .chrome-bottom {
    position: absolute; left: 0; top: 666px; width: 100%; height: 59px;
    background: linear-gradient(180deg, #0c0c0d 0 10px, #c9cdd1 10px 13px, #25272a 13px 30px, #7c8288 30px 34px, #000 34px 100%);
  }
</style>
</head>
<body>
  <article class="flyer">
    <div class="chrome-top"></div>
    <div class="header-bar"></div>
    <div class="accent-bar"></div>
    <h1 class="firm-name">MARVELLO QUINTARD LLP</h1>

    <div class="slogan-band"></div>
    <p class="slogan">You Speak. We Listen. They Pay.</p>

    <div class="name-box"><span class="name-box-text">Marvello Quintard LLP</span></div>

    <div class="main-panel"></div>
    <div class="contact-bar"></div>

    <address class="contact-info">
      <div class="address">752 W. Folbrook Lane, Suite 400 Beverly Hills, CA 90210</div>
      <div>phone: <strong>310.555.8143</strong></div>
      <div>fax: <strong>310.555.9261</strong></div>
      <div>email: <strong>info@mqmlegal.example</strong></div>
      <div>web: <strong>www.mqmlegal.example</strong></div>
    </address>

    <div class="partner-photo" role="img" aria-label="Group photo of the firm's three partners in business attire"></div>

    <h2 class="practice-head" style="top:213px">Personal Injury</h2>
    <div class="practice-icon" style="top:254px" role="img" aria-label="Ambulance icon"></div>
    <p class="practice-copy" style="top:247px">If you or a loved one are suffering from an injury or wrongful death caused by the careless or intentional acts of others, then you have the right to pursue compensation for your injury, out-of-pocket expenses, lost wages, emotional anguish, and more.</p>

    <h2 class="practice-head" style="top:375px">Employment Law</h2>
    <div class="practice-icon" style="top:411px" role="img" aria-label="Person at computer desk icon"></div>
    <p class="practice-copy" style="top:407px">Our attorneys regularly represent clients in disputes involving sex, age and race discrimination, sexual harassment, retaliatory discharge, defamation, unlawful termination, breach of employment contracts, and more.</p>

    <p class="contact-callout">CONTACT US FOR A <b>FREE CONSULTATION TODAY</b></p>

    <div class="chrome-bottom"></div>
  </article>
</body>
</html>
```